Tallowmere Crest Partners

Please look at the logo that we've just received and based on it provide us with the business card designs.

Industry/Entity Type

Business

Requirements
Must have
• Dummy text, so later on we can add the exact names and titles.

```html
<!DOCTYPE html>
<html lang="en">
<head>
<meta charset="utf-8">
<title>Tallowmere Crest Partners – Business Cards</title>
<link href="https://fonts.googleapis.com/css2?family=Marcellus&family=Didact+Gothic&display=swap" rel="stylesheet">
<style>
  :root {
    --backdrop: #e9e7e3;
    --paper: #f7f7f6;
    --brand-blue: #23419a;
    --deep-blue: #1d3a8c;
    --steel-grey: #9b9ea3;
    --text-grey: #6d6f73;
    --white: #ffffff;
  }
  * { margin: 0; padding: 0; box-sizing: border-box; }
  html, body { width: 1200px; height: 911px; overflow: hidden; }
  body {
    background: var(--backdrop);
    font-family: "Didact Gothic", sans-serif;
    position: relative;
  }
  .card {
    position: absolute;
    top: 158px;
    width: 340px;
    height: 595px;
    box-shadow: 0 10px 26px rgba(0,0,0,0.18);
  }
  /* Front */
  .card--front { left: 220px; background: var(--paper); }
  .band {
    position: absolute;
    top: 40px;
    height: 90px;
    width: 100%;
    display: flex;
  }
  .band__blue { flex: 0 0 50%; background: var(--brand-blue); }
  .band__grey { flex: 1; background: var(--steel-grey); }
  .brand-square {
    position: absolute;
    top: 55px;
    left: 50%;
    width: 60px;
    height: 60px;
    margin-left: -30px;
    background: var(--white);
    border: 5px solid var(--deep-blue);
  }
  .wordmark {
    position: absolute;
    top: 160px;
    width: 100%;
    text-align: center;
    font-family: "Marcellus", serif;
    font-weight: 400;
    color: var(--brand-blue);
  }
  .wordmark__main { display: block; font-size: 32px; letter-spacing: 1px; line-height: 1.1; }
  .wordmark__sub { display: block; font-size: 12px; letter-spacing: 5px; margin-top: 4px; }
  .contact {
    position: absolute;
    top: 268px;
    width: 100%;
    text-align: center;
    color: var(--text-grey);
    font-size: 15px;
    line-height: 1.45;
  }
  .contact__name {
    font-family: "Marcellus", serif;
    color: var(--brand-blue);
    font-size: 22px;
    letter-spacing: 1px;
  }
  .contact__title { font-size: 14px; letter-spacing: 0.5px; }
  .rule {
    width: 26px;
    height: 2px;
    background: var(--brand-blue);
    margin: 12px auto;
  }
  /* Back */
  .card--back { left: 640px; background: var(--brand-blue); }
  .back__mark {
    position: absolute;
    bottom: 60px;
    left: 30px;
    right: 20px;
    color: var(--white);
    font-family: "Marcellus", serif;
  }
  .back__main { display: block; font-size: 32px; letter-spacing: 1px; line-height: 1.1; }
  .back__sub { display: block; font-size: 12px; letter-spacing: 5px; margin-top: 4px; }
  .back__web {
    margin-top: 6px;
    font-family: "Didact Gothic", sans-serif;
    font-size: 13px;
    letter-spacing: 0.5px;
  }
</style>
</head>
<body>
  <section class="card card--front" aria-label="Business card front">
    <div class="band"><div class="band__blue"></div><div class="band__grey"></div></div>
    <div class="brand-square"></div>
    <h1 class="wordmark">
      <span class="wordmark__main">TALLOWMERE</span>
      <span class="wordmark__sub">CREST PARTNERS</span>
    </h1>
    <div class="contact">
      <p class="contact__name">JORDAN AVERY</p>
      <p class="contact__title">CEO/FOUNDER</p>
      <div class="rule"></div>
      <p>4120 Larchmont Way</p>
      <p>Fairbrook, Oregon 97812</p>
      <div class="rule"></div>
      <p>555 214 7390</p>
      <p>hello@tallowmerecrest.com</p>
      <p>www.tallowmerecrest.com</p>
    </div>
  </section>

  <section class="card card--back" aria-label="Business card back">
    <div class="back__mark">
      <p>
        <span class="back__main">TALLOWMERE</span>
        <span class="back__sub">CREST PARTNERS</span>
      </p>
      <p class="back__web">www.tallowmerecrestpartners.com</p>
    </div>
  </section>
</body>
</html>
```